Logo & Visitenkarte für Logopädische Praxis
Zielgruppe
In meiner logopädischen Praxis geht es um Sprach-, Sprech- und Stimmtherapie. Meine Zielgruppe sind Erwachsene jeglichen Alters und Geschlechts.
Aufgabenstellung
Ich habe noch keine konkreten Vorstellungen.

```html
<!DOCTYPE html>
<html lang="de">
<head>
<meta charset="utf-8">
<title>Fridolin Kuberz – Logopädische Praxis – Visitenkarte</title>
<link href="https://fonts.googleapis.com/css2?family=Exo+2:wght@500;600;700&display=swap" rel="stylesheet">
<style>
  :root {
    --teal: #237f95;
    --green: #5c9a1f;
    --white: #ffffff;
    --stage: #ecebe8;
  }
  * { margin: 0; padding: 0; box-sizing: border-box; }
  html, body { width: 1200px; height: 969px; overflow: hidden; background: var(--stage); }
  body { position: relative; font-family: "Exo 2", sans-serif; }

  .card { position: absolute; overflow: hidden; }
  .card--front { left: 284px; top: 48px; width: 643px; height: 415px; background: var(--teal); color: var(--white); }
  .card--back { left: 285px; top: 486px; width: 637px; height: 403px; background: var(--white); }

  .brand { position: absolute; left: 0; right: 0; text-align: center; }
  .brand__dot { position: absolute; border-radius: 50%; left: 50%; transform: translateX(-50%); }
  .brand__name { position: absolute; left: 0; right: 0; font-weight: 700; letter-spacing: 0.5px; line-height: 1; }
  .brand__tag { position: absolute; left: 0; right: 0; font-weight: 600; line-height: 1; }

  .card--front .brand__dot { top: 98px; width: 144px; height: 144px; background: var(--white); }
  .card--front .brand__name { top: 262px; font-size: 36px; }
  .card--front .brand__tag { top: 300px; font-size: 17px; letter-spacing: 7.6px; padding-left: 7px; }

  .card--back .brand__dot { top: 47px; width: 106px; height: 106px; background: var(--teal); }
  .card--back .brand__name { top: 163px; font-size: 27px; color: var(--teal); }
  .card--back .brand__tag { top: 195px; font-size: 13px; letter-spacing: 5.8px; padding-left: 6px; color: var(--green); }

  .wave { position: absolute; left: 0; top: 0; width: 637px; height: 403px; }

  .contact { position: absolute; display: flex; align-items: center; color: var(--white); font-weight: 600; }
  .contact__icon { width: 30px; height: 30px; border-radius: 50%; background: var(--white); display: flex; align-items: center; justify-content: center; flex: none; }
  .contact__icon svg { width: 18px; height: 18px; }
  .contact__text { margin-left: 19px; }

  .contact--web { left: 20px; top: 306px; font-size: 14px; }
  .contact--address { left: 20px; top: 353px; }
  .contact--address .contact__text { font-size: 11px; line-height: 13.5px; margin-top: -14px; }
  .contact--address .contact__icon { align-self: flex-start; }
  .contact--phone { left: 355px; top: 256px; font-size: 16px; }
  .contact--fax { left: 355px; top: 306px; font-size: 18px; }
  .contact--mail { left: 355px; top: 359px; font-size: 14px; }
  .contact--mail .contact__text { margin-left: 8px; }
  .contact--phone .contact__text, .contact--fax .contact__text { margin-left: 10px; }
</style>
</head>
<body>

<section class="card card--front">
  <div class="brand">
    <span class="brand__dot"></span>
    <p class="brand__name">FRIDOLIN KUBERZ</p>
    <p class="brand__tag">LOGOPÄDISCHE PRAXIS</p>
  </div>
</section>

<section class="card card--back">
  <div class="brand">
    <span class="brand__dot"></span>
    <p class="brand__name">FRIDOLIN KUBERZ</p>
    <p class="brand__tag">LOGOPÄDISCHE PRAXIS</p>
  </div>

  <svg class="wave" viewBox="0 0 637 403" aria-hidden="true">
    <path d="M0 244 C120 285 260 285 400 235 C480 208 560 205 637 218 L637 223 C560 212 480 216 400 243 C260 292 120 292 0 252 Z" fill="var(--teal)"/>
    <path d="M0 270 C110 305 230 300 320 265 L320 272 C230 310 110 318 0 290 Z" fill="var(--green)"/>
    <path d="M0 262 C140 300 280 300 420 245 C500 215 570 218 637 254 L637 403 L0 403 Z" fill="var(--teal)"/>
  </svg>

  <div class="contact contact--web">
    <span class="contact__icon">
      <svg viewBox="0 0 24 24" fill="none" stroke="var(--teal)" stroke-width="1.8"><circle cx="12" cy="12" r="9"/><ellipse cx="12" cy="12" rx="4" ry="9"/><path d="M3 12h18M5 7h14M5 17h14"/></svg>
    </span>
    <span class="contact__text">WWW.KIEFERPRAXIS-LINDHOLM.DE</span>
  </div>

  <div class="contact contact--address">
    <span class="contact__icon">
      <svg viewBox="0 0 24 24"><path d="M12 2a7 7 0 0 0-7 7c0 5 7 13 7 13s7-8 7-13a7 7 0 0 0-7-7zm0 9.5A2.5 2.5 0 1 1 12 6.5a2.5 2.5 0 0 1 0 5z" fill="var(--teal)"/></svg>
    </span>
    <span class="contact__text">KIEFERORTHOPÄDISCHE FACHZAHNARZTPRAXIS<br>HENRIK SOLMSDORF,<br>TALWEG 27<br>31842 LINDHOLM</span>
  </div>

  <div class="contact contact--phone">
    <span class="contact__icon">
      <svg viewBox="0 0 24 24"><path d="M6.6 10.8a15 15 0 0 0 6.6 6.6l2.2-2.2a1 1 0 0 1 1-.25 11.4 11.4 0 0 0 3.6.57 1 1 0 0 1 1 1V20a1 1 0 0 1-1 1A17 17 0 0 1 3 4a1 1 0 0 1 1-1h3.5a1 1 0 0 1 1 1c0 1.25.2 2.45.57 3.57a1 1 0 0 1-.25 1z" fill="var(--teal)"/></svg>
    </span>
    <span class="contact__text">0481-552307</span>
  </div>

  <div class="contact contact--fax">
    <span class="contact__icon">
      <svg viewBox="0 0 24 24"><path d="M7 3h10v5H7zM5 9h14a2 2 0 0 1 2 2v6h-4v4H7v-4H3v-6a2 2 0 0 1 2-2zm4 6v4h6v-4z" fill="var(--teal)"/></svg>
    </span>
    <span class="contact__text">0481-552318</span>
  </div>

  <div class="contact contact--mail">
    <span class="contact__icon">
      <svg viewBox="0 0 24 24"><path d="M3 6h18v12H3z" fill="var(--teal)"/><path d="M3 6l9 7 9-7M3 18l7-6M21 18l-7-6" fill="none" stroke="var(--white)" stroke-width="1.4"/></svg>
    </span>
    <span class="contact__text">info@kieferpraxis-lindholm.de</span>
  </div>
</section>

</body>
</html>
```